Postcard Design

Cinder Vale Partners is a waste and Recycling company. We want to purchase recyclable materials from businesses. We would like to use the colors green and grey. The exact colors needed in this project are described below. We would like to have a picture of waste cardboard,a picture of money, and and the line- Are you getting top dollar for your Recyclables? After please put our logo and our phone number: 800.742.5196, our website (bronlomar.com),
and our email address: marisol@bronlomar.com.

* Postcard must contain our logo. Please see buisness card for branding

Industry/Entity Type

It Company

Requirements
Must have
• This postcard must contain the logo and these colors:
Pantone: 576C & 418C

```html
<!DOCTYPE html>
<html lang="en">
<head>
<meta charset="utf-8">
<title>Cinder Vale Partners – Recyclables Postcard</title>
<link href="https://fonts.googleapis.com/css2?family=Open+Sans:wght@400;600;700&display=swap" rel="stylesheet">
<style>
  :root {
    --green: #6cbf2e;
    --green-light: #cfe8b8;
    --grey: #51534a;
    --grey-band: #5a6157;
    --text-grey: #4a4a44;
    --stage: #0d0d0d;
    --white: #ffffff;
    --stamp: #e4e6e2;
  }
  * { margin: 0; padding: 0; box-sizing: border-box; }
  html, body { width: 1200px; height: 1000px; overflow: hidden; }
  body { background: var(--stage); font-family: "Open Sans", Arial, sans-serif; position: relative; }

  .card { position: absolute; background: var(--white); overflow: hidden; width: 661px; height: 511px; }
  .card-back { left: 32px; top: 72px; }
  .card-front { left: 488px; top: 420px; box-shadow: -18px 12px 40px rgba(0,0,0,.35); }

  .brand { position: absolute; display: flex; align-items: center; gap: 8px; color: var(--grey); font-weight: 700; white-space: nowrap; }
  .brand-mark { background: var(--green); border-radius: 50%; flex: none; }
  .card-back .brand { left: 50px; top: 30px; font-size: 23px; }
  .card-back .brand-mark { width: 28px; height: 28px; }

  .stamp-box { position: absolute; left: 506px; top: 26px; width: 129px; height: 128px; background: var(--stamp); opacity: .85; }
  .back-band { position: absolute; left: 0; top: 70px; width: 661px; height: 94px; background: var(--green); }
  .photo-circle { position: absolute; top: 74px; width: 86px; height: 86px; border-radius: 50%; border: 4px solid var(--white); box-shadow: 0 3px 6px rgba(0,0,0,.25); }
  .photo-money { left: 38px; background: radial-gradient(circle, #b9c4a8, #6f7d63); }
  .photo-bulb { left: 122px; background: radial-gradient(circle, #ffffff, #dcdcdc); }
  .photo-bags { left: 206px; background: linear-gradient(180deg, #a9b6bf 0%, #3c3f44 55%, #1e1f22 100%); }
  .stamp-box { z-index: 2; }
  .back-headline { position: absolute; left: 320px; top: 84px; color: var(--white); font-size: 15px; line-height: 20px; z-index: 3; }
  .back-headline strong { font-size: 23px; font-weight: 700; }

  .back-copy { position: absolute; left: 20px; top: 188px; width: 340px; text-align: center; color: var(--text-grey); font-size: 13.5px; line-height: 18px; }
  .back-copy .emph { color: var(--green); font-weight: 700; margin: 8px 0 5px; }
  .back-contact { position: absolute; left: 20px; top: 337px; width: 340px; text-align: center; color: var(--text-grey); }
  .phone { font-weight: 700; color: var(--grey); }
  .back-contact .phone { font-size: 26px; line-height: 36px; }
  .back-contact .line { font-size: 15px; line-height: 23px; }

  .front-art { position: absolute; left: 0; top: 0; }
  .front-headline { position: absolute; left: 0; top: 28px; width: 661px; text-align: center; color: var(--white); font-size: 28px; line-height: 38px; }
  .front-headline b { font-weight: 700; }
  .photo-money-hand { position: absolute; left: 250px; top: 124px; width: 212px; height: 128px; background: linear-gradient(135deg, #e9eddf, #9aa88a 60%, #d9b9a0); border-radius: 6px; }
  .photo-cardboard { position: absolute; left: 28px; top: 160px; width: 335px; height: 315px; background: linear-gradient(180deg, #cfb48c, #b89567 70%, #2a2a2a 100%); border-radius: 8px; }
  .card-front .brand { left: 336px; top: 280px; font-size: 26px; }
  .card-front .brand-mark { width: 40px; height: 40px; }
  .front-contact { position: absolute; left: 394px; top: 336px; color: var(--grey); }
  .front-contact .phone { font-size: 35px; line-height: 48px; font-weight: 600; }
  .front-contact .line { font-size: 18px; line-height: 26px; }
  .front-footer { position: absolute; left: 0; top: 425px; width: 661px; height: 86px; background: var(--grey-band); }
  .front-footer .web { position: absolute; left: 412px; top: 11px; color: var(--white); font-size: 18px; }
</style>
</head>
<body>

<section class="card card-back">
  <div class="brand"><span class="brand-mark"></span>Cinder Vale Partners</div>
  <div class="stamp-box"></div>
  <div class="back-band"></div>
  <div class="photo-circle photo-money" role="img" aria-label="Stack of dollar bills"></div>
  <div class="photo-circle photo-bulb" role="img" aria-label="Light bulb with a green sprout inside"></div>
  <div class="photo-circle photo-bags" role="img" aria-label="Pile of black garbage bags in a city"></div>
  <h2 class="back-headline"><strong>Stop</strong> Hemorrhaging<br>Money With Your<br>Waste Bill!</h2>
  <div class="back-copy">
    <p>We have the expertise, experience, and, just as important, connections to help you efficiently and swiftly cut costs.</p>
    <p class="emph">And it costs you NOTHING out of pocket.</p>
    <p>If you are looking to save 20-70% of your monthly waste bill, and don't want to spend a penny out of pocket, contact us today!</p>
  </div>
  <div class="back-contact">
    <p class="phone">800.742.5196</p>
    <p class="line">marisol@bronlomar.com</p>
    <p class="line">www.bronlomar.com</p>
  </div>
</section>

<section class="card card-front">
  <svg class="front-art" width="661" height="511" viewBox="0 0 661 511">
    <rect width="661" height="200" fill="var(--green)"/>
    <path d="M0 150 C160 120 420 112 661 200 L661 220 C430 140 180 140 0 150 Z" fill="var(--green-light)"/>
    <path d="M0 150 C180 140 430 140 661 220 L661 511 L0 511 Z" fill="var(--white)"/>
  </svg>
  <h1 class="front-headline">Are you getting top<br><b>dollar</b> for your <b>Recyclables?</b></h1>
  <div class="photo-money-hand" role="img" aria-label="Hand in a suit sleeve holding out a bundle of dollar bills"></div>
  <div class="photo-cardboard" role="img" aria-label="Figure made of cardboard boxes reclining in an office chair"></div>
  <div class="front-footer"><span class="web">www.bronlomar.com</span></div>
  <div class="brand"><span class="brand-mark"></span>Cinder Vale Partners</div>
  <div class="front-contact">
    <p class="phone">800.742.5196</p>
    <p class="line">marisol@bronlomar.com</p>
  </div>
</section>

</body>
</html>
```